Stationery Design needed for logo design project

This company needs a letterhead and envelope for their new practice. We did not want to release this contact until the business card design was finalized so the stationary can be created to coordinate with it.

For those of you that will be submitting designs for this content, think "linear". Designs with curves or "swooshes" are not appropriate for this design.

NOTE: As part of the source files; I will require FULLY LAYERED PHOTOSHOP FILES of all elements, including design elements, text and fonts. If you cannot provide a fully layered PSD file, please do not submit.
Updates

The project details have been updated. We have added a new description along with logo files and business card design. Please review the style of the logo and business card before submitting designs. Thanks

Target Market(s)

Medical

Industry/Entity Type

Business

Requirements
Must have
• NOTE: As part of the source files; I will require FULLY LAYERED PHOTOSHOP FILES of all elements, including design elements, text and fonts. If you cannot provide a fully layered PSD file, please do not submit.

Logo
2 office address locations
phone
fax
email
website URL

```html
<!DOCTYPE html>
<html lang="en">
<head>
<meta charset="utf-8">
<title>Harlan &amp; Associates — Stationery</title>
<link href="https://fonts.googleapis.com/css2?family=Cinzel:wght@500&family=Lato:wght@400;700&display=swap" rel="stylesheet">
<style>
:root{
  --bg:#cdcdcd;
  --paper:#ececec;
  --paper-bright:#f3f3f3;
  --ink:#1b1b1b;
  --red:#b3262d;
  --black:#0e0e0e;
  --muted:#6b6b6b;
  --rule:#bdbdbd;
}
*{margin:0;padding:0;box-sizing:border-box}
html,body{width:1200px;height:1000px;overflow:hidden;background:var(--bg)}
.canvas{position:relative;width:1200px;height:1000px;font-family:"Lato",Arial,sans-serif}
.sheet{position:absolute;background:var(--paper);overflow:hidden}
.folder{left:83px;top:267px;width:341px;height:455px}
.letterhead{left:452px;top:282px;width:313px;height:440px;background:var(--paper-bright)}
.envelope-front{left:798px;top:363px;width:329px;height:163px;background:var(--paper-bright)}
.envelope-back{left:800px;top:553px;width:328px;height:166px;background:var(--paper-bright)}

.brand{position:absolute;display:flex;align-items:center;white-space:nowrap}
.brand .dot{border-radius:50%;background:var(--red);flex:none}
.brand .name{font-family:"Cinzel",Georgia,serif;font-weight:500;color:var(--ink);letter-spacing:.02em}
.folder .brand{left:88px;top:76px;gap:10px}
.folder .brand .dot{width:22px;height:22px}
.folder .brand .name{font-size:19px}
.letterhead .brand{left:19px;top:30px;gap:6px}
.letterhead .brand .dot{width:13px;height:13px}
.letterhead .brand .name{font-size:11px}
.envelope-front .brand{left:15px;top:17px;gap:5px}
.envelope-front .brand .dot{width:11px;height:11px}
.envelope-front .brand .name{font-size:9.5px}

.footer-band{position:absolute;left:0;bottom:0;width:100%;height:18px;display:block}
.envelope-front .footer-band{height:12px}

.contact{position:absolute;display:flex;font-size:3.6px;line-height:1.45;color:var(--muted)}
.contact h4{color:var(--red);font-size:3.8px;font-weight:700}
.contact .office, .contact .lines{display:flex;flex-direction:column}
.letterhead .contact{left:20px;bottom:24px;gap:42px}
.envelope-front .contact{left:18px;bottom:16px;gap:44px;font-size:3.2px}
.envelope-front .contact h4{font-size:3.4px}

.flap{position:absolute;left:0;top:0;width:100%;height:64px;display:block}
.flap-brand{position:absolute;left:132px;top:20px;display:flex;align-items:center;gap:5px}
.flap-brand .dot{width:10px;height:10px;border-radius:50%;background:var(--red)}
.flap-brand .name{font-family:"Cinzel",Georgia,serif;font-weight:500;font-size:9px;color:#f1f1f1}
</style>
</head>
<body>
<main class="canvas">

  <section class="sheet folder" aria-label="Presentation folder">
    <div class="brand"><span class="dot"></span><span class="name">Harlan &amp; Associates</span></div>
    <svg class="footer-band" viewBox="0 0 341 18" preserveAspectRatio="none">
      <rect x="0" y="6" width="262" height="1" fill="var(--rule)"/>
      <rect x="0" y="9" width="262" height="4" fill="var(--red)"/>
      <polygon points="266,0 341,0 341,18 250,18" fill="var(--black)"/>
      <circle cx="306" cy="9" r="3.5" fill="none" stroke="#fff" stroke-width="0.8"/>
    </svg>
  </section>

  <section class="sheet letterhead" aria-label="Letterhead">
    <div class="brand"><span class="dot"></span><span class="name">Harlan &amp; Associates</span></div>
    <div class="contact">
      <div class="office"><h4>Downtown Office</h4><span>214 Linden Pl NE, Suite 12</span><span>Fairview, NM 87104</span><span>(555) 014-2287</span></div>
      <div class="office"><h4>West Side Office</h4><span>580 Mesa Ridge Rd, Suite 203</span><span>Cedar Falls, NM 87126</span><span>(555) 014-2290</span></div>
      <div class="lines"><span>555-0199-42</span><span>care@harlanheart.example</span><span>www.harlanheart.example</span></div>
    </div>
    <svg class="footer-band" viewBox="0 0 313 18" preserveAspectRatio="none">
      <rect x="0" y="6" width="245" height="1" fill="var(--rule)"/>
      <rect x="0" y="9" width="245" height="4" fill="var(--red)"/>
      <polygon points="248,0 313,0 313,18 234,18" fill="var(--black)"/>
      <circle cx="281" cy="9" r="3.5" fill="none" stroke="#fff" stroke-width="0.8"/>
    </svg>
  </section>

  <section class="sheet envelope-front" aria-label="Envelope front">
    <div class="brand"><span class="dot"></span><span class="name">Harlan &amp; Associates</span></div>
    <div class="contact">
      <div class="office"><h4>Downtown Office</h4><span>214 Linden Pl NE, Suite 12</span><span>Fairview, NM 87104</span><span>(555) 014-2287</span></div>
      <div class="office"><h4>West Side Office</h4><span>580 Mesa Ridge Rd, Suite 203</span><span>Cedar Falls, NM 87126</span><span>(555) 014-2290</span></div>
      <div class="lines"><span>555-0199-42</span><span>care@harlanheart.example</span><span>www.harlanheart.example</span></div>
    </div>
    <svg class="footer-band" viewBox="0 0 329 12" preserveAspectRatio="none">
      <rect x="0" y="4" width="255" height="0.8" fill="var(--rule)"/>
      <rect x="0" y="6" width="255" height="3" fill="var(--red)"/>
      <polygon points="258,0 329,0 329,12 246,12" fill="var(--black)"/>
      <circle cx="292" cy="6" r="3" fill="none" stroke="#fff" stroke-width="0.7"/>
    </svg>
  </section>

  <section class="sheet envelope-back" aria-label="Envelope back">
    <svg class="flap" viewBox="0 0 328 64" preserveAspectRatio="none">
      <polygon points="0,0 328,0 322,60 6,60" fill="var(--black)"/>
    </svg>
    <div class="flap-brand"><span class="dot"></span><span class="name">Harlan &amp; Associates</span></div>
  </section>

</main>
</body>
</html>
```